Medical service promotional magnet representing our 7 day service.

Please design a magnet in the number 7 to represent a 7 day service. The size needs to be no more than 80mmx90mm be bright and show the service has 2 businesses that cover the 7 days. The logos are added to assist. Perhaps 2 puzzle pieces or something similar would be good.
We have
Norvale Clinic Link Nightcare
Open Monday to Friday 6-10pm
Saturday 1pm - 10pm
Sunday and public holidays 9am -10pm.
Phone 74119352

Also have the locum service

Norvale Ring For Care
Open Monday to Thursday 6pm - 8am
Friday 6pm to Monday 8am
Public holidays 24 hours.
Phone 741196083

Hi Designers,
Could you design a magnet in the shape of a number 7 please. If you can include the logos that would be great. The 7 represents the 7 days a week - perhaps the 7 could be made of 2 puzzle pieces making the number 7 including both logos and colours. We look forward to seeing your designs.
Cheers Bea and Team.

```html
<!DOCTYPE html>
<html lang="en">
<head>
<meta charset="utf-8">
<title>7 Day Service Magnet</title>
<link rel="stylesheet" href="https://fonts.googleapis.com/css2?family=Jost:wght@400;700&display=swap">
<style>
  :root {
    --page: #ffffff;
    --locum-red: #e32b2b;
    --clinic-blue: #1b95d0;
    --ink-white: #ffffff;
    --ink-dark: #231f20;
  }
  html, body {
    margin: 0;
    padding: 0;
    width: 1200px;
    height: 1000px;
    overflow: hidden;
    background: var(--page);
  }
  .magnet {
    display: block;
    width: 1200px;
    height: 1000px;
    font-family: "Jost", "Futura", sans-serif;
  }
  .panel-red { fill: var(--locum-red); }
  .panel-blue { fill: var(--clinic-blue); }
  .numeral { fill: var(--ink-white); }
  .service-name { fill: var(--ink-white); font-weight: 700; font-size: 33px; }
  .hours { fill: var(--ink-white); font-weight: 400; font-size: 20.5px; }
  .phone { fill: var(--ink-dark); font-weight: 700; font-size: 26px; }
  .headline { fill: var(--ink-white); font-weight: 700; font-size: 74px; }
  .align-right { text-anchor: end; }
</style>
</head>
<body>
<svg class="magnet" viewBox="0 0 1200 1000" xmlns="http://www.w3.org/2000/svg" role="img" aria-label="7 Day Service magnet for Norvale Ring For Care and Norvale Clinic Link Nightcare">
  <!-- card halves -->
  <rect class="panel-blue" x="297" y="145" width="620" height="695"/>
  <path class="panel-red" d="M297 145 H917 V495 A86 86 0 0 0 745 495 H471 A86.5 86.5 0 0 1 298 495 H297 Z"/>

  <!-- large numeral seven -->
  <path class="numeral" d="M377 312 H638 V352 C565 440 508 560 487 682 H432 C452 560 512 440 588 356 H377 Z"/>

  <!-- locum service -->
  <g class="align-right">
    <text class="service-name" x="897" y="182">Norvale Ring For Care</text>
    <text class="hours" x="897" y="210">Mon to Thurs 6pm-8am</text>
    <text class="hours" x="897" y="242">Friday 6pm to Monday 8am</text>
    <text class="hours" x="897" y="274">Public holidays 24 hours.</text>
    <text class="phone" x="897" y="311">Phone 741196083</text>
  </g>

  <!-- headline -->
  <text class="headline" x="602" y="473">Day</text>
  <text class="headline" x="552" y="563">Service</text>

  <!-- clinic service -->
  <text class="service-name" x="314" y="725">Norvale Clinic Link Nightcare</text>
  <text class="hours" x="314" y="757">Mon to Fri 6-10pm Sat 1-10pm</text>
  <text class="hours" x="314" y="790">Sunday &amp; public holidays 9am -10pm</text>
  <text class="phone" x="314" y="823">Phone 74119352</text>
</svg>
</body>
</html>
```